TovaLamarpe - Israeli Mental Health Website

We are developing an Israeli website for mental health. The website will be both in English and in Hebrew. We have a logo and would like a website design based on the logo and the logos colors (attached).

Attached is a doc that contains the website requirements.

We would like to have an icon for each of the sidebar categories, an image for each of the pages (including each of the sidebar category pages).

Target Market(s)

Adults 18-80

Industry/Entity Type

Mental Health

Number of Pages Required

5+ page

Font styles to use
Sans Serif

Colors

Designer to choose colors to be used in the design.

```html
<!DOCTYPE html>
<html lang="en">
<head>
<meta charset="utf-8">
<title>TovaLamarpe – Floating Menu Concept</title>
<link href="https://fonts.googleapis.com/css2?family=Roboto:wght@400;500;700;900&display=swap" rel="stylesheet">
<style>
:root{
  --blue:#1f70c8;
  --green:#4fae3f;
  --navy:#141c3a;
  --ink:#1c1c1c;
  --icon:#2f2f33;
  --panel:rgba(244,246,246,.93);
  --white:#ffffff;
}
*{box-sizing:border-box;margin:0;padding:0}
html,body{width:1200px;height:687px;overflow:hidden;background:#fff;font-family:'Roboto',sans-serif;color:var(--ink)}
.canvas{position:relative;width:1200px;height:687px}
.annotation{position:absolute;top:26px;font-size:8.5px;font-weight:700;color:#000}
.annotation-line{position:absolute;top:0;left:0;overflow:visible}
.site{position:absolute;top:65px;width:498px;height:548px;overflow:hidden;background:var(--navy)}
.site--collapsed{left:57px}
.site--expanded{left:632px}
.hero{position:absolute;left:0;top:0;width:498px;height:282px;
  background:linear-gradient(90deg,#f1f1f0 0%,#e9e8e6 35%,#d9d3cc 60%,#a89384 78%,#5c4a40 100%)}
.band{position:absolute;left:0;top:282px;width:498px;height:141px;background:var(--green)}
.nav{position:absolute;top:13px;height:12px;background:var(--blue);color:var(--white);font-size:6.4px;font-weight:700;
  display:flex;align-items:center;justify-content:center;border-radius:1px}
.lang{position:absolute;left:433px;top:14px;width:59px;height:10px;display:flex;border:1px solid var(--green);background:var(--white);font-size:5.4px}
.lang span{flex:1;display:flex;align-items:center;justify-content:center}
.lang .on{background:var(--green);color:var(--white)}
.hero-title{position:absolute;left:87px;top:80px;font-size:17px;font-weight:500;letter-spacing:.2px}
.hero-text{position:absolute;left:87px;top:110px;width:172px;font-size:6.2px;line-height:6.7px;font-weight:500}
.phone{position:absolute;left:87px;top:180px;width:108px;height:22px;border:1.5px solid var(--green);border-radius:11px;background:rgba(255,255,255,.6);
  font-size:10px;padding-left:29px;display:flex;align-items:center}
.phone-badge{position:absolute;left:-2px;top:-2px;width:25px;height:25px;border-radius:50%;background:var(--green)}
.card{position:absolute;width:92px;height:98px;background:var(--blue);border-radius:2px;overflow:hidden}
.card-media{position:absolute;left:0;top:0;width:92px;height:51px}
.card-title{position:absolute;left:9px;top:27px;font-size:10.5px;line-height:11.5px;font-weight:700;color:var(--white)}
.card-text{position:absolute;left:9px;top:57px;width:78px;font-size:5.4px;line-height:6.2px;color:var(--white)}
.chat-dot{position:absolute;left:48px;top:3px;width:26px;height:26px;border-radius:6px;background:var(--green)}
.sidebar{position:absolute;left:0;top:0;width:66px;height:307px;background:var(--panel);border-radius:0 6px 6px 0}
.sidebar--open{width:177px;backdrop-filter:blur(3px)}
.brand-mark{position:absolute;left:32px;top:12px;width:20px;height:20px;border-radius:50%;border:2px solid var(--blue)}
.sidebar--open .brand-mark{left:31px}
.brand-name{position:absolute;left:60px;top:13px;font-size:16px;font-weight:700;color:var(--green)}
.menu-icon{position:absolute;left:37px;width:11px;height:11px}
.menu-label{position:absolute;left:60px;font-size:5.3px;font-weight:700;color:#111}
.footer-brand{position:absolute;left:65px;top:443px;display:flex;align-items:center;gap:4px;color:var(--white);font-size:12px;font-weight:700}
.footer-brand i{width:16px;height:16px;border-radius:50%;border:1.5px solid var(--white)}
.footer-text{position:absolute;left:65px;top:467px;width:128px;font-size:6.6px;line-height:7.4px;color:var(--white)}
.social{position:absolute;top:508px;width:6px;height:6px;border-radius:50%;background:var(--white)}
.footer-heading{position:absolute;top:437px;color:var(--white);font-size:8.2px}
.footer-heading--bold{font-weight:700}
.footer-links{position:absolute;top:451px;list-style:none;color:var(--white);font-size:6.6px;line-height:12.4px}
.news-text{position:absolute;left:332px;top:453px;width:110px;font-size:4.2px;line-height:7.5px;color:#c9cde0}
.news-form{position:absolute;left:332px;top:470px;width:102px;height:12px;display:flex;border:1px solid #8c93b3;border-radius:2px;background:var(--navy)}
.news-form span{font-size:4.4px;display:flex;align-items:center}
.news-input{flex:1;color:#8c93b3;padding-left:4px}
.news-btn{width:25px;justify-content:center;background:var(--white);color:#222}
.copyright{position:absolute;left:0;top:530px;width:498px;text-align:center;font-size:6.6px;color:#c9cde0}
</style>
</head>
<body>
<div class="canvas">

  <p class="annotation" style="left:43px">Floting Menu With Hover Animation</p>
  <p class="annotation" style="left:576px">Floting Menu With Hover Animation</p>
  <svg class="annotation-line" width="1200" height="80">
    <g stroke="#222" stroke-width=".6" fill="none">
      <path d="M91 38 L97 70 M93 67 L97 70 L101 66"/>
      <path d="M717 38 L723 70 M719 67 L723 70 L727 66"/>
    </g>
  </svg>

  <!-- Collapsed state -->
  <section class="site site--collapsed">
    <div class="hero" role="img" aria-label="Photo of a doctor in a white coat consulting a worried patient"></div>
    <div class="band"></div>

    <div class="nav" style="left:102px;width:50px">Therapists</div>
    <div class="nav" style="left:157px;width:61px">Organizations</div>
    <div class="nav" style="left:223px;width:39px">Videos</div>
    <div class="nav" style="left:268px;width:42px">Contact</div>
    <div class="nav" style="left:314px;width:38px">About</div>
    <div class="nav" style="left:357px;width:40px">Donate</div>
    <div class="lang"><span class="on">English</span><span>עברית</span></div>

    <h1 class="hero-title">HERO REXT HERE</h1>
    <p class="hero-text">Lorem Ipsum Dolor Sit Amet, Consectetur Adipiscing Elit, Sed Do Eiusmod Tempor Incididunt Ut Labore Et Dolore Magna Aliqua. Ut Enim Ad Minim Veniam, Quis Nostrud Exercitation Ullamco Laboris Nisi Ut Aliquip Ex Ea Commodo Consequat. Duis Aute Irure Dolor In Reprehenderit In Voluptate Velit Esse Cillum Dolore Eu Fugiat Nulla Pariatur. Excepteur Sint Occaecat Cupidatat Non Proident, Sunt In Culpa Qui Officia Deserunt Mollit Anim Id Est Laborum.</p>
    <div class="phone"><span class="phone-badge"><svg width="25" height="25" viewBox="0 0 25 25"><path d="M8 7c1-1 2 0 2.5 1.5l.5 1.5c0 .8-1 1.2-1 1.8.6 1.6 2 3 3.6 3.6.6 0 1-1 1.8-1l1.5.5c1.5.5 2.5 1.5 1.5 2.5-1 1.2-2.5 1.5-4 .8C11 17 8 14 7.2 11 6.6 9.5 7 8 8 7z" fill="#fff"/></svg></span>000 0000 00000</div>

    <article class="card" style="left:73px;top:211px"><div class="card-media" role="img" aria-label="Photo of a distressed person on the phone" style="background:linear-gradient(135deg,#6b5a52,#c9b4a6 60%,#3d302c)"></div><h2 class="card-title">Emergency<br>Mental Help</h2><p class="card-text">Lorem Ipsum Dolor Sit Amet, Consectetur Adipiscing Elit, Sed Do Eiusmod Tempor Incididunt Ut</p></article>
    <article class="card" style="left:177px;top:211px"><div class="card-media" role="img" aria-label="Green glowing chat background" style="background:linear-gradient(135deg,#0c2d16,#1f8a3a 55%,#06140a)"></div><span class="chat-dot"></span><h2 class="card-title">Smart<br>Chat</h2><p class="card-text">Lorem Ipsum Dolor Sit Amet, Consectetur Adipiscing Elit, Sed Do Eiusmod Tempor Incididunt Ut</p></article>
    <article class="card" style="left:282px;top:211px"><div class="card-media" role="img" aria-label="Photo of a therapy session" style="background:linear-gradient(135deg,#c7b7a8,#4b5d7d 60%,#2a3450)"></div><h2 class="card-title" style="top:38px">Therapists</h2><p class="card-text">Lorem Ipsum Dolor Sit Amet, Consectetur Adipiscing Elit, Sed Do Eiusmod Tempor Incididunt Ut</p></article>

    <article class="card" style="left:125px;top:315px"><div class="card-media" role="img" aria-label="Photo of a cheering group outdoors" style="background:linear-gradient(135deg,#3f5a3a,#8a8f86 55%,#243a58)"></div><h2 class="card-title" style="top:38px">Organizations</h2><p class="card-text">Lorem Ipsum Dolor Sit Amet, Consectetur Adipiscing Elit, Sed Do Eiusmod Tempor Incididunt Ut</p></article>
    <article class="card" style="left:229px;top:315px"><div class="card-media" role="img" aria-label="Photo of people watching a video together" style="background:linear-gradient(135deg,#2e3a58,#8b7a82 55%,#3b2f3a)"></div><h2 class="card-title" style="top:38px">Videos</h2><p class="card-text">Lorem Ipsum Dolor Sit Amet, Consectetur Adipiscing Elit, Sed Do Eiusmod Tempor Incididunt Ut</p></article>
    <article class="card" style="left:333px;top:315px"><div class="card-media" role="img" aria-label="Digital padlock security illustration" style="background:radial-gradient(circle at 60% 40%,#3d7cc9,#0f2a55 70%)"></div><h2 class="card-title" style="top:38px">Privacy Policy</h2><p class="card-text">Lorem Ipsum Dolor Sit Amet, Consectetur Adipiscing Elit, Sed Do Eiusmod Tempor Incididunt Ut</p></article>

    <nav class="sidebar">
      <span class="brand-mark"></span>
      <svg class="menu-icon" style="top:48px" viewBox="0 0 11 11" role="img" aria-label="Emergency mental help"><circle cx="5.5" cy="5.5" r="5" fill="#2f2f33"/></svg>
      <svg class="menu-icon" style="top:68px" viewBox="0 0 11 11" role="img" aria-label="Suicide"><circle cx="5.5" cy="5.5" r="5" fill="#2f2f33"/></svg>
      <svg class="menu-icon" style="top:88px" viewBox="0 0 11 11" role="img" aria-label="Sexual assault victims"><circle cx="5.5" cy="5.5" r="5" fill="#2f2f33"/></svg>
      <svg class="menu-icon" style="top:107px" viewBox="0 0 11 11" role="img" aria-label="Sexual assault offenders"><circle cx="5.5" cy="5.5" r="5" fill="#2f2f33"/></svg>
      <svg class="menu-icon" style="top:127px" viewBox="0 0 11 11" role="img" aria-label="Post trauma"><circle cx="5.5" cy="5.5" r="5" fill="#2f2f33"/></svg>
      <svg class="menu-icon" style="top:147px" viewBox="0 0 11 11" role="img" aria-label="Depression"><circle cx="5.5" cy="5.5" r="5" fill="#2f2f33"/></svg>
      <svg class="menu-icon" style="top:166px" viewBox="0 0 11 11" role="img" aria-label="Anxiety"><circle cx="5.5" cy="5.5" r="5" fill="#2f2f33"/></svg>
      <svg class="menu-icon" style="top:186px" viewBox="0 0 11 11" role="img" aria-label="Addictions"><circle cx="5.5" cy="5.5" r="5" fill="#2f2f33"/></svg>
      <svg class="menu-icon" style="top:206px" viewBox="0 0 11 11" role="img" aria-label="Sleep disorders"><circle cx="5.5" cy="5.5" r="5" fill="#2f2f33"/></svg>
      <svg class="menu-icon" style="top:225px" viewBox="0 0 11 11" role="img" aria-label="Eating disorders"><circle cx="5.5" cy="5.5" r="5" fill="#2f2f33"/></svg>
      <svg class="menu-icon" style="top:245px" viewBox="0 0 11 11" role="img" aria-label="Financial problems"><circle cx="5.5" cy="5.5" r="5" fill="#2f2f33"/></svg>
      <svg class="menu-icon" style="top:265px" viewBox="0 0 11 11" role="img" aria-label="Parenthood"><circle cx="5.5" cy="5.5" r="5" fill="#2f2f33"/></svg>
      <svg class="menu-icon" style="top:284px" viewBox="0 0 11 11" role="img" aria-label="Relationship"><circle cx="5.5" cy="5.5" r="5" fill="#2f2f33"/></svg>
    </nav>

    <div class="footer-brand"><i></i>TovaLamarpe</div>
    <p class="footer-text">Lorem Ipsum Dolor Sit Amet, Consectetur Adipiscing Elit, Sed Do Eiusmod Tempor Incididunt Ut Labore Et Dolore Magna Aliqua. Ut Enim Ad Minim Veniam</p>
    <span class="social" style="left:66px"></span><span class="social" style="left:79px"></span><span class="social" style="left:92px"></span>
    <h3 class="footer-heading footer-heading--bold" style="left:201px">Navigations</h3>
    <ul class="footer-links" style="left:201px"><li>Therapists</li><li>Organizations</li><li>Videos</li><li>Contact</li><li>About</li><li>Donate</li></ul>
    <ul class="footer-links" style="left:261px;top:438px"><li>Privacy Policy</li><li>Terms</li></ul>
    <h3 class="footer-heading" style="left:332px">Subscribe Newsletter</h3>
    <p class="news-text">Lorem Ipsum Dolor Sit Amet, Consectetur Doler Adipiscing Elit.</p>
    <div class="news-form"><span class="news-input">Enter Email</span><span class="news-btn">Subscribe</span></div>
    <p class="copyright">TovaLamarpe - Organization For Mental Health ©2023</p>
  </section>

  <!-- Expanded state -->
  <section class="site site--expanded">
    <div class="hero" role="img" aria-label="Photo of a doctor in a white coat consulting a worried patient"></div>
    <div class="band"></div>

    <div class="nav" style="left:102px;width:50px">Therapists</div>
    <div class="nav" style="left:157px;width:61px">Organizations</div>
    <div class="nav" style="left:223px;width:39px">Videos</div>
    <div class="nav" style="left:268px;width:42px">Contact</div>
    <div class="nav" style="left:314px;width:38px">About</div>
    <div class="nav" style="left:357px;width:40px">Donate</div>
    <div class="lang"><span class="on">English</span><span>עברית</span></div>

    <h1 class="hero-title">HERO REXT HERE</h1>
    <p class="hero-text">Lorem Ipsum Dolor Sit Amet, Consectetur Adipiscing Elit, Sed Do Eiusmod Tempor Incididunt Ut Labore Et Dolore Magna Aliqua. Ut Enim Ad Minim Veniam, Quis Nostrud Exercitation Ullamco Laboris Nisi Ut Aliquip Ex Ea Commodo Consequat. Duis Aute Irure Dolor In Reprehenderit In Voluptate Velit Esse Cillum Dolore Eu Fugiat Nulla Pariatur. Excepteur Sint Occaecat Cupidatat Non Proident, Sunt In Culpa Qui Officia Deserunt Mollit Anim Id Est Laborum.</p>
    <div class="phone"><span class="phone-badge"></span>000 0000 00000</div>

    <article class="card" style="left:73px;top:211px"><div class="card-media" role="img" aria-label="Photo of a distressed person on the phone" style="background:linear-gradient(135deg,#6b5a52,#c9b4a6 60%,#3d302c)"></div><h2 class="card-title">Emergency<br>Mental Help</h2><p class="card-text">Lorem Ipsum Dolor Sit Amet, Consectetur Adipiscing Elit, Sed Do Eiusmod Tempor Incididunt Ut</p></article>
    <article class="card" style="left:177px;top:211px"><div class="card-media" role="img" aria-label="Green glowing chat background" style="background:linear-gradient(135deg,#0c2d16,#1f8a3a 55%,#06140a)"></div><span class="chat-dot"></span><h2 class="card-title">Smart<br>Chat</h2><p class="card-text">Lorem Ipsum Dolor Sit Amet, Consectetur Adipiscing Elit, Sed Do Eiusmod Tempor Incididunt Ut</p></article>
    <article class="card" style="left:282px;top:211px"><div class="card-media" role="img" aria-label="Photo of a therapy session" style="background:linear-gradient(135deg,#c7b7a8,#4b5d7d 60%,#2a3450)"></div><h2 class="card-title" style="top:38px">Therapists</h2><p class="card-text">Lorem Ipsum Dolor Sit Amet, Consectetur Adipiscing Elit, Sed Do Eiusmod Tempor Incididunt Ut</p></article>

    <article class="card" style="left:125px;top:315px"><div class="card-media" role="img" aria-label="Photo of a cheering group outdoors" style="background:linear-gradient(135deg,#3f5a3a,#8a8f86 55%,#243a58)"></div><h2 class="card-title" style="top:38px">Organizations</h2><p class="card-text">Lorem Ipsum Dolor Sit Amet, Consectetur Adipiscing Elit, Sed Do Eiusmod Tempor Incididunt Ut</p></article>
    <article class="card" style="left:229px;top:315px"><div class="card-media" role="img" aria-label="Photo of people watching a video together" style="background:linear-gradient(135deg,#2e3a58,#8b7a82 55%,#3b2f3a)"></div><h2 class="card-title" style="top:38px">Videos</h2><p class="card-text">Lorem Ipsum Dolor Sit Amet, Consectetur Adipiscing Elit, Sed Do Eiusmod Tempor Incididunt Ut</p></article>
    <article class="card" style="left:333px;top:315px"><div class="card-media" role="img" aria-label="Digital padlock security illustration" style="background:radial-gradient(circle at 60% 40%,#3d7cc9,#0f2a55 70%)"></div><h2 class="card-title" style="top:38px">Privacy Policy</h2><p class="card-text">Lorem Ipsum Dolor Sit Amet, Consectetur Adipiscing Elit, Sed Do Eiusmod Tempor Incididunt Ut</p></article>

    <nav class="sidebar sidebar--open">
      <span class="brand-mark"></span>
      <span class="brand-name">TovaLamarpe</span>
      <svg class="menu-icon" style="top:48px" viewBox="0 0 11 11" role="img" aria-label="Emergency mental help"><circle cx="5.5" cy="5.5" r="5" fill="#2f2f33"/></svg><span class="menu-label" style="top:50px">Emergency Mental Help</span>
      <svg class="menu-icon" style="top:68px" viewBox="0 0 11 11" role="img" aria-label="Suicide"><circle cx="5.5" cy="5.5" r="5" fill="#2f2f33"/></svg><span class="menu-label" style="top:70px">Icon Suicide</span>
      <svg class="menu-icon" style="top:88px" viewBox="0 0 11 11" role="img" aria-label="Sexual assault victims"><circle cx="5.5" cy="5.5" r="5" fill="#2f2f33"/></svg><span class="menu-label" style="top:90px">Icon Sexual Assault/Violence Victims</span>
      <svg class="menu-icon" style="top:107px" viewBox="0 0 11 11" role="img" aria-label="Sexual assault offenders"><circle cx="5.5" cy="5.5" r="5" fill="#2f2f33"/></svg><span class="menu-label" style="top:110px">Icon Sexual Assault/Violence Assaulters</span>
      <svg class="menu-icon" style="top:127px" viewBox="0 0 11 11" role="img" aria-label="Post trauma"><circle cx="5.5" cy="5.5" r="5" fill="#2f2f33"/></svg><span class="menu-label" style="top:129px">Icon Post Trauma</span>
      <svg class="menu-icon" style="top:147px" viewBox="0 0 11 11" role="img" aria-label="Depression"><circle cx="5.5" cy="5.5" r="5" fill="#2f2f33"/></svg><span class="menu-label" style="top:149px">Icon Depression</span>
      <svg class="menu-icon" style="top:166px" viewBox="0 0 11 11" role="img" aria-label="Anxiety"><circle cx="5.5" cy="5.5" r="5" fill="#2f2f33"/></svg><span class="menu-label" style="top:169px">Icon Anxiety</span>
      <svg class="menu-icon" style="top:186px" viewBox="0 0 11 11" role="img" aria-label="Addictions"><circle cx="5.5" cy="5.5" r="5" fill="#2f2f33"/></svg><span class="menu-label" style="top:188px">Icon Addictions</span>
      <svg class="menu-icon" style="top:206px" viewBox="0 0 11 11" role="img" aria-label="Sleep disorders"><circle cx="5.5" cy="5.5" r="5" fill="#2f2f33"/></svg><span class="menu-label" style="top:208px">Sleep Disorders</span>
      <svg class="menu-icon" style="top:225px" viewBox="0 0 11 11" role="img" aria-label="Eating disorders"><circle cx="5.5" cy="5.5" r="5" fill="#2f2f33"/></svg><span class="menu-label" style="top:228px">Eating Disorders</span>
      <svg class="menu-icon" style="top:245px" viewBox="0 0 11 11" role="img" aria-label="Financial problems"><circle cx="5.5" cy="5.5" r="5" fill="#2f2f33"/></svg><span class="menu-label" style="top:247px">Financial Problems</span>
      <svg class="menu-icon" style="top:265px" viewBox="0 0 11 11" role="img" aria-label="Parenthood"><circle cx="5.5" cy="5.5" r="5" fill="#2f2f33"/></svg><span class="menu-label" style="top:267px">Parenthood</span>
      <svg class="menu-icon" style="top:284px" viewBox="0 0 11 11" role="img" aria-label="Relationship"><circle cx="5.5" cy="5.5" r="5" fill="#2f2f33"/></svg><span class="menu-label" style="top:287px">Relationship</span>
    </nav>

    <div class="footer-brand"><i></i>TovaLamarpe</div>
    <p class="footer-text">Lorem Ipsum Dolor Sit Amet, Consectetur Adipiscing Elit, Sed Do Eiusmod Tempor Incididunt Ut Labore Et Dolore Magna Aliqua. Ut Enim Ad Minim Veniam</p>
    <span class="social" style="left:66px"></span><span class="social" style="left:79px"></span><span class="social" style="left:92px"></span>
    <h3 class="footer-heading footer-heading--bold" style="left:201px">Navigations</h3>
    <ul class="footer-links" style="left:201px"><li>Therapists</li><li>Organizations</li><li>Videos</li><li>Contact</li><li>About</li><li>Donate</li></ul>
    <ul class="footer-links" style="left:261px;top:438px"><li>Privacy Policy</li><li>Terms</li></ul>
    <h3 class="footer-heading" style="left:332px">Subscribe Newsletter</h3>
    <p class="news-text">Lorem Ipsum Dolor Sit Amet, Consectetur Doler Adipiscing Elit.</p>
    <div class="news-form"><span class="news-input">Enter Email</span><span class="news-btn">Subscribe</span></div>
    <p class="copyright">TovaLamarpe - Organization For Mental Health ©2023</p>
  </section>

</div>
</body>
</html>
```